Birgit Hollmer - Entwicklung für Menschen und Organisationen
Kreative Ideen, die sehr professionell umgesetzt werden und selbstständig verbesserte Versionen werden zur Verfügung gestellt. DANKE!
Zielgruppe
Ich biete Organisationsentwicklungen, Coachings, Teamentwicklungen, Moderationen, Führungskräfteentwicklung, Konfliktklärung und Seminare an.
Meine Zielgruppe sind Vorstände, Geschäftsführer, Personaler, Führungskräfte und andere 'Entscheider'.
Aufgabenstellung
Das Format soll in ein DIN lang Kuvert passen, jedoch gerne nicht das klassische zweifach-gefaltete A4 sein.
Es soll zu meinem Logo und den Druckstücken passen.
Es soll herauskommen, dass alle Leistungen in der Organisationsentwicklung enthalten sein können, diese jedoch auch jeweils einzeln angeboten werden können.
Ich benötige die Broschüre als "offene" Datei, da ich in naher Zukunft die Geschäftsräume wechsele.

```html
<!DOCTYPE html>
<html lang="de">
<head>
<meta charset="utf-8">
<title>Birgit Hollmer – Flyer</title>
<link rel="stylesheet" href="https://fonts.googleapis.com/css2?family=Signika:wght@400;600&family=Roboto+Condensed:wght@700&display=swap">
<style>
  :root {
    --red: #e0252b;
    --red-deep: #a91d22;
    --ink: #1d1d1f;
    --ink-soft: #2a2a2c;
    --page: #e6e7e9;
    --white: #ffffff;
  }
  * { box-sizing: border-box; margin: 0; padding: 0; }
  html, body { width: 1200px; height: 2626px; overflow: hidden; }
  body { background: var(--page); font-family: "Signika", sans-serif; position: relative; }

  .spread {
    position: absolute; left: 60px; top: 930px;
    width: 1080px; height: 766px;
    display: flex;
  }
  .panel { position: relative; width: 360px; height: 100%; overflow: hidden; }

  /* left panel */
  .panel--about { background: var(--red); color: var(--white); }
  .panel--about .deco-circle {
    position: absolute; left: 200px; top: 140px; width: 170px; height: 170px;
    border-radius: 50%; background: var(--red-deep); opacity: .55;
  }
  .section-title {
    position: absolute; left: 18px; font-weight: 600; font-size: 29px;
    padding: 0 0 4px 18px; border-bottom: 2px solid var(--white);
  }
  .section-title--about { top: 26px; width: 166px; }
  .section-title--offer { top: 412px; width: 220px; }
  .copy {
    position: absolute; left: 36px; width: 300px;
    font-size: 16.5px; line-height: 22.3px;
  }
  .copy p + p { margin-top: 22px; }
  .copy--about { top: 102px; }
  .copy--offer { top: 480px; }

  /* middle panel */
  .panel--contact { background: var(--ink); color: var(--white); text-align: center; }
  .puzzle-photo {
    position: absolute; left: 0; top: 0; width: 100%; height: 470px;
    background: linear-gradient(180deg, #6c6c6e 0%, #4a4a4c 45%, #2e2e30 80%, var(--ink) 100%);
  }
  .contact-name {
    position: absolute; top: 392px; left: 0; width: 100%;
    font-size: 30px; font-weight: 400;
  }
  .contact-details {
    position: absolute; top: 470px; left: 0; width: 100%;
    font-size: 13.5px; line-height: 17px;
  }
  .contact-details p + p { margin-top: 16px; }
  .contact-details b { font-weight: 600; }

  /* right panel */
  .panel--cover { background: var(--ink-soft); color: var(--white); border-left: 1px solid #3a3a3c; }
  .portrait {
    position: absolute; left: 40px; top: 60px; width: 320px; height: 560px;
    background: radial-gradient(ellipse at 55% 40%, #b8a58a 0%, #6e6256 40%, #3a3637 70%, var(--ink-soft) 100%);
  }
  .brand-mark { position: absolute; left: 28px; top: 28px; display: flex; align-items: center; gap: 10px; }
  .brand-mark .square { width: 72px; height: 72px; border-radius: 6px; background: var(--red); }
  .brand-mark .name { font-size: 14px; font-weight: 400; color: var(--white); }
  .cover-title {
    position: absolute; left: 36px; top: 522px;
    font-family: "Roboto Condensed", sans-serif; font-weight: 700;
    font-size: 40px; line-height: 50px; letter-spacing: .2px;
  }
  .url-band {
    position: absolute; right: 0; top: 716px; width: 200px; height: 27px;
    background: var(--red); font-size: 13.5px; line-height: 27px; text-align: center;
  }
</style>
</head>
<body>
  <main class="spread">
    <section class="panel panel--about">
      <div class="deco-circle"></div>
      <h2 class="section-title section-title--about">Über mich</h2>
      <div class="copy copy--about">
        <p>Mit meinen über 12 Jahren Erfahrung in der Personal- und Unternehmensentwicklung unterstütze ich Sie gerne bei Ihren Veränderungsprozessen und helfe Ihnen Probleme zu lösen.</p>
        <p>Mit mir profitieren Sie von der Verbindung der beiden Welten: der Mitarbeiterorientierung sowie die erfolgsorientierten Unternehmensentwicklung.</p>
      </div>
      <h2 class="section-title section-title--offer">Mein Angebot</h2>
      <div class="copy copy--offer">
        <p>Mein Angebot ist Organisationsentwicklung als Ganzes, d.h. die sechs weiteren genannten</p>
        <p>Leistungen können ein Teil davon sein – je nach Prozess. Zusätzlich biete ich die sechs</p>
        <p>Leistungen auch individuell an. Das soll im Flyer raus kommen!!!</p>
      </div>
    </section>

    <section class="panel panel--contact">
      <div class="puzzle-photo" role="img" aria-label="Schwarz-weißes Foto verstreuter Puzzleteile"></div>
      <h3 class="contact-name">Birgit Hollmer</h3>
      <div class="contact-details">
        <p>Talgrund 9<br>90999 Musterfeld</p>
        <p><b>T:</b> 0911 / 5550 1201<br><b>F:</b> 0911/ 5550 1202<br><b>H:</b> 0170 / 55 50 123</p>
        <p><b>Mail:</b><br>kontakt@birgit-hollmer.de</p>
        <p><b>Website:</b><br>www.birgit-hollmer.de</p>
      </div>
    </section>

    <section class="panel panel--cover">
      <div class="portrait" role="img" aria-label="Porträtfoto der Beraterin im dunklen Blazer"></div>
      <div class="brand-mark"><span class="square"></span><span class="name">Birgit Hollmer</span></div>
      <h1 class="cover-title">Entwicklung<br>für Menschen und<br>Organisationen</h1>
      <div class="url-band">www.birgit-hollmer.de</div>
    </section>
  </main>
</body>
</html>
```